Vireo M.K. - Diagnostic Ultrasound Flyer

About US
Vireo M.K. is a concierge ultrasound company that provides onsite or offsite diagnostic ultrasounds. We have over 14 years experience in sonography, business management, and customer service. We offer both the physician and patient flexibility, convenience, and access to timely services.

We provide ultrasounds for the following specialties:
Obstetrics/Gynecology
Abdominal
Small Parts
Vascular

Company Features:
1. Onsite or Offsite Scans
2. Images Available Immediately for Referring Physician and Patient
3. Flexible Options for Ultrasound Interpretation/Billing
4. Access to Interpreting Radiologist
5. Final Report Process - 1-2 Business Days/ 1 hour for STAT.
6. PACS Storage with Secure Access.

We need a place to add in our contact information (address, email, website, phone)

We already have a logo and would like to use it ( they are attached). We would the colors to match the logo colors....maybe lighter version of yellow and blue.

```html
<!DOCTYPE html>
<html lang="en">
<head>
<meta charset="utf-8">
<title>Vireo M.K. – Diagnostic Ultrasound Flyer</title>
<link rel="stylesheet" href="https://fonts.googleapis.com/css2?family=Montserrat:ital,wght@0,400;0,500;0,700;0,800;1,700;1,800&display=swap">
<style>
  :root {
    --blue: #2f59c9;
    --blue-deep: #2448b0;
    --navy: #1a1f9e;
    --yellow: #fdbf2d;
    --yellow-soft: #fdd57c;
    --white: #ffffff;
    --ink: #1d1d1f;
    --paper: #f6f7f9;
    --stage: #e4e4e4;
  }
  * { margin: 0; padding: 0; box-sizing: border-box; }
  html, body { width: 909px; height: 1200px; overflow: hidden; }
  body { background: var(--stage); font-family: "Montserrat", Arial, sans-serif; position: relative; }

  .flyer { position: absolute; left: 30px; top: 0; width: 849px; height: 1200px; overflow: hidden; background: var(--paper); }
  .flyer-shapes { position: absolute; inset: 0; }

  .headline { position: absolute; left: 43px; top: 46px; color: var(--white); font-style: italic; font-weight: 800; font-size: 39px; line-height: 43px; letter-spacing: -0.3px; }
  .headline .accent { color: var(--yellow); }
  .about { position: absolute; left: 43px; top: 366px; width: 305px; color: var(--white); font-size: 14.6px; line-height: 20.4px; }

  .brand { position: absolute; left: 555px; top: 48px; display: flex; align-items: center; gap: 9px; }
  .brand-dot { width: 14px; height: 14px; border-radius: 50%; background: var(--yellow); }
  .brand-name { color: var(--navy); font-weight: 800; font-size: 33px; letter-spacing: 1px; }

  .photo { position: absolute; }
  .photo-machine { left: 362px; top: 93px; width: 204px; height: 526px; border-radius: 14px; background: linear-gradient(180deg, #dfe4ea 0%, #c9d0d9 55%, #9ea7b3 100%); }
  .photo-round { width: 172px; height: 172px; border-radius: 50%; border: 6px solid var(--blue); background: linear-gradient(145deg, #e9eef5 0%, #c8d3e2 60%, #e7c9b3 100%); }
  .photo-1 { left: 613px; top: 135px; }
  .photo-2 { left: 613px; top: 287px; background: linear-gradient(145deg, #eef2f7 0%, #b7c3d3 70%, #7d8aa0 100%); }
  .photo-3 { left: 613px; top: 438px; background: linear-gradient(145deg, #cfd8e6 0%, #eddccd 55%, #d9b9a3 100%); }

  .tab { position: absolute; height: 32px; display: flex; align-items: center; color: var(--white); font-style: italic; font-weight: 800; letter-spacing: 5px; transform: skewX(-10deg); background: linear-gradient(90deg, var(--blue) 0%, var(--blue) 75%, rgba(47,89,201,0) 100%); }
  .tab span { transform: skewX(10deg); display: block; }
  .tab-features { left: 60px; top: 656px; width: 281px; padding-left: 8px; font-size: 19px; }
  .tab-specialties { left: 522px; top: 738px; width: 260px; padding-left: 8px; font-size: 20px; }
  .features-icon { position: absolute; left: 18px; top: 654px; width: 32px; height: 32px; }

  .features { position: absolute; left: 34px; top: 730px; list-style: none; width: 400px; }
  .features li { display: flex; gap: 10px; font-size: 17px; line-height: 27px; color: var(--ink); margin-bottom: 9.5px; }
  .features svg { flex: none; width: 14px; height: 14px; margin-top: 6px; }

  .specialty-icon { position: absolute; left: 524px; width: 46px; height: 46px; border-radius: 10px; background: rgba(47,89,201,0.18); }
  .specialty { position: absolute; left: 593px; color: var(--blue); font-weight: 700; font-size: 21px; line-height: 21px; }
  .divider { position: absolute; left: 593px; width: 180px; border-top: 1px dotted var(--blue); }

  .contact { position: absolute; color: var(--yellow-soft); font-size: 20px; line-height: 24px; }
  .contact-label { left: 160px; top: 1078px; }
  .contact-phone { left: 160px; top: 1101px; color: var(--yellow-soft); font-weight: 800; font-size: 30px; line-height: 34px; letter-spacing: 1px; }
  .contact-address { left: 160px; top: 1153px; }
  .contact-web { left: 497px; top: 1113px; color: var(--white); }
  .contact-mail { left: 497px; top: 1151px; color: var(--white); }
  .contact-icon { position: absolute; width: 26px; height: 26px; }
</style>
</head>
<body>
<main class="flyer">
  <svg class="flyer-shapes" width="849" height="1200" viewBox="0 0 849 1200" aria-hidden="true">
    <rect x="0" y="0" width="849" height="720" fill="var(--blue)"/>
    <path d="M478 0 H849 V648 C 770 646, 650 625, 560 605 C 530 598, 500 596, 478 596 Z" fill="var(--paper)"/>
    <path d="M0 560 C 120 520, 240 520, 330 560 C 390 585, 440 600, 478 606" fill="none" stroke="var(--blue-deep)" stroke-width="14" opacity="0.45"/>
    <path d="M0 702 C 130 738, 300 735, 478 690 L478 1200 H0 Z" fill="var(--paper)"/>
    <path d="M0 668 C 70 628, 160 604, 235 605 C 310 607, 375 628, 430 651 C 350 700, 260 724, 175 723 C 105 722, 45 708, 0 694 Z" fill="var(--yellow-soft)"/>
    <path d="M478 690 C 560 705, 640 716, 705 707 C 770 698, 815 684, 849 676 V1200 H478 Z" fill="var(--yellow-soft)"/>
    <path d="M0 1058 H392 L450 1083 H849 V1200 H0 Z" fill="var(--blue)"/>
  </svg>

  <h1 class="headline">
    CONCIERGE<br>ULTRASOUND<br>PROVIDES<br><span class="accent">ONSITE</span> OR<br><span class="accent">OFFSITE</span><br>DIAGNOSTIC<br>ULTRASOUNDS
  </h1>
  <p class="about">We have over 14 years experience in sonography, business management and customer service. We offer both the physician and patient flexibility, convenience, and access to timely services.</p>

  <div class="brand"><span class="brand-dot"></span><span class="brand-name">Vireo M.K.</span></div>

  <div class="photo photo-machine" role="img" aria-label="Cart-based ultrasound scanner with monitor and control panel"></div>
  <div class="photo photo-round photo-1" role="img" aria-label="Sonographer scanning a patient's arm with a probe"></div>
  <div class="photo photo-round photo-2" role="img" aria-label="Hand pointing at an ultrasound monitor"></div>
  <div class="photo photo-round photo-3" role="img" aria-label="Ultrasound probe on a patient's abdomen"></div>

  <svg class="features-icon" viewBox="0 0 32 32" aria-hidden="true">
    <circle cx="19" cy="8" r="5" fill="none" stroke="var(--blue)" stroke-width="2.4"/>
    <circle cx="19" cy="8" r="1.8" fill="var(--blue)"/>
    <rect x="2" y="18" width="5" height="12" fill="var(--blue)"/>
    <path d="M8 20 H16 C20 20 22 23 20 24 H13 M8 28 H20 L29 21 C30 19 28 17 26 18 L20 22" fill="none" stroke="var(--blue)" stroke-width="2.4" stroke-linejoin="round"/>
  </svg>
  <div class="tab tab-features"><span>OUR FEATURES</span></div>

  <ul class="features">
    <li><svg viewBox="0 0 14 14"><rect x="0.7" y="0.7" width="12.6" height="12.6" fill="none" stroke="var(--ink)" stroke-width="1.2"/><path d="M3 7 L6 10 L11.5 2.5" fill="none" stroke="var(--ink)" stroke-width="1.4"/></svg><span>Onsite or Offsite Scans</span></li>
    <li><svg viewBox="0 0 14 14"><rect x="0.7" y="0.7" width="12.6" height="12.6" fill="none" stroke="var(--ink)" stroke-width="1.2"/><path d="M3 7 L6 10 L11.5 2.5" fill="none" stroke="var(--ink)" stroke-width="1.4"/></svg><span>Images Available Immediately for<br>Referring Physician and Patient</span></li>
    <li><svg viewBox="0 0 14 14"><rect x="0.7" y="0.7" width="12.6" height="12.6" fill="none" stroke="var(--ink)" stroke-width="1.2"/><path d="M3 7 L6 10 L11.5 2.5" fill="none" stroke="var(--ink)" stroke-width="1.4"/></svg><span>Flexible Options for Ultrasound<br>Interpretation/Billing</span></li>
    <li><svg viewBox="0 0 14 14"><rect x="0.7" y="0.7" width="12.6" height="12.6" fill="none" stroke="var(--ink)" stroke-width="1.2"/><path d="M3 7 L6 10 L11.5 2.5" fill="none" stroke="var(--ink)" stroke-width="1.4"/></svg><span>Access to Interpreting Radiologist</span></li>
    <li><svg viewBox="0 0 14 14"><rect x="0.7" y="0.7" width="12.6" height="12.6" fill="none" stroke="var(--ink)" stroke-width="1.2"/><path d="M3 7 L6 10 L11.5 2.5" fill="none" stroke="var(--ink)" stroke-width="1.4"/></svg><span>Final Report Process - 1-2 Business<br>Days/ 1 hour for STAT.</span></li>
    <li><svg viewBox="0 0 14 14"><rect x="0.7" y="0.7" width="12.6" height="12.6" fill="none" stroke="var(--ink)" stroke-width="1.2"/><path d="M3 7 L6 10 L11.5 2.5" fill="none" stroke="var(--ink)" stroke-width="1.4"/></svg><span>PACS Storage with Secure Access.</span></li>
  </ul>

  <div class="tab tab-specialties"><span>SPECIALTIES</span></div>

  <div class="specialty-icon" style="top:806px" role="img" aria-label="Line icon of a uterus for obstetrics and gynecology"></div>
  <div class="specialty" style="top:806px">OBSTETRICS/<br>GYNECOLOGY</div>
  <div class="divider" style="top:864px"></div>
  <div class="specialty-icon" style="top:868px" role="img" aria-label="Line icon of abdominal organs"></div>
  <div class="specialty" style="top:881px">ABDOMINAL</div>
  <div class="divider" style="top:926px"></div>
  <div class="specialty-icon" style="top:938px" role="img" aria-label="Line icon of small organs"></div>
  <div class="specialty" style="top:951px">SMALL PARTS</div>
  <div class="divider" style="top:988px"></div>
  <div class="specialty-icon" style="top:1002px" role="img" aria-label="Line icon of a heart with vessels"></div>
  <div class="specialty" style="top:1015px">VASCULAR</div>

  <svg class="contact-icon" style="left:118px;top:1092px;width:32px;height:32px" viewBox="0 0 32 32" aria-hidden="true">
    <path d="M9 4 L13 11 L10 14 C11 18 14 21 18 22 L21 19 L28 23 L25 28 C14 28 4 18 4 7 Z" fill="none" stroke="var(--white)" stroke-width="2.4" stroke-linejoin="round"/>
    <path d="M19 4 A9 9 0 0 1 28 13 M19 9 A4 4 0 0 1 23 13" fill="none" stroke="var(--white)" stroke-width="2.2"/>
  </svg>
  <div class="contact contact-label">For More Information</div>
  <div class="contact contact-phone">123 456 7890</div>

  <svg class="contact-icon" style="left:114px;top:1152px" viewBox="0 0 26 26" aria-hidden="true">
    <circle cx="13" cy="13" r="13" fill="var(--white)"/>
    <path d="M13 20 C9 15 8 13 8 11 A5 5 0 0 1 18 11 C18 13 17 15 13 20 Z" fill="var(--blue)"/>
    <circle cx="13" cy="11" r="2" fill="var(--white)"/>
  </svg>
  <div class="contact contact-address">Place Your Address Here</div>

  <svg class="contact-icon" style="left:459px;top:1115px" viewBox="0 0 26 26" aria-hidden="true">
    <circle cx="13" cy="13" r="13" fill="var(--white)"/>
    <g fill="none" stroke="var(--blue)" stroke-width="1.4">
      <circle cx="13" cy="13" r="7"/><ellipse cx="13" cy="13" rx="3" ry="7"/><path d="M6 13 H20 M7.5 9.5 H18.5 M7.5 16.5 H18.5"/>
    </g>
  </svg>
  <div class="contact contact-web">www.yourwebsite.com</div>

  <svg class="contact-icon" style="left:459px;top:1152px" viewBox="0 0 26 26" aria-hidden="true">
    <circle cx="13" cy="13" r="13" fill="var(--white)"/>
    <rect x="6.5" y="8.5" width="13" height="9" fill="none" stroke="var(--blue)" stroke-width="1.5"/>
    <path d="M6.5 8.5 L13 14 L19.5 8.5" fill="none" stroke="var(--blue)" stroke-width="1.5"/>
  </svg>
  <div class="contact contact-mail">email.yourwebsite.com</div>
</main>
</body>
</html>
```